Simple and clean webdesign for personal homepage

Trying to create a simple and clean webdesign for my personal homepage. Going to use a static site builder with templates to build the site. I want it to have multiple pages - like an about me, blog and resume. I just need something very basic I can customize. I want the main colors to be purple, black and white. I am open to other color palettes too but since purple is my favorite color I want that to be one of the main colors.

The site be mostly text driven. Might have some images in the body text but I want the site design to be light and lean.

Industry/Entity Type

Personal Homepage.

Coding

Coded - Design and coding required

Number of Pages Required

1 page

Font styles to use
Sans Serif

Colors
6B429C
8869AF
B7A5CE
E3DAEB
F3F0F8

Requirements
Must have
• Clean design. Purple used as a color. HTML template.
Nice to have
• Responsive

```html
<!DOCTYPE html>
<html lang="en">
<head>
<meta charset="utf-8">
<title>Mira Solen — Personal Homepage</title>
<link rel="stylesheet" href="https://fonts.googleapis.com/css2?family=Montserrat:ital,wght@0,400;0,500;0,600;0,700;0,800;1,500&display=swap">
<style>
:root{
  --purple:#6b21c8;
  --purple-bright:#7b2fd6;
  --purple-soft:#b7a5ce;
  --lilac:#e2cff3;
  --lilac-band:#c6aeea;
  --lilac-card:#e8dbfb;
  --ink:#0b0b10;
  --text:#333;
  --muted:#777;
  --white:#fff;
}
*{margin:0;padding:0;box-sizing:border-box}
html,body{width:1200px;height:3856px;overflow:hidden}
body{font-family:"Montserrat",sans-serif;color:var(--ink);background:var(--white);position:relative}
.abs{position:absolute}

/* hero */
.hero{position:absolute;left:0;top:0;width:1200px;height:775px;background:#030308}
.sidebar{position:absolute;left:0;top:0;width:72px;height:775px;background:var(--purple)}
.sidebar svg{position:absolute;left:25px;width:14px;height:14px}
.hero-photo{position:absolute;left:72px;top:0;width:540px;height:775px;
  background:radial-gradient(ellipse at 55% 30%,#6b4a3a 0%,#2e1d16 35%,#0a0707 70%,#030308 100%)}
.hero-name{position:absolute;left:760px;top:320px;font-size:58px;font-weight:800;color:var(--purple-bright);letter-spacing:1px}
.hero-tag{position:absolute;left:761px;top:413px;font-size:10.5px;font-style:italic;font-weight:500;color:#fff;line-height:13px}
.social{position:absolute;left:761px;top:472px;display:flex;gap:18px;font-size:11px;font-weight:700;color:#fff}

/* about */
.about{position:absolute;left:0;top:775px;width:1200px;height:595px;background:var(--lilac)}
.h-section{position:absolute;font-size:34px;font-weight:800;color:var(--ink)}
.rule{position:absolute;height:3px;width:167px;background:var(--purple)}
.about p{position:absolute;left:177px;width:460px;font-size:10.5px;line-height:19.5px;color:#222}
.about .fact{font-weight:700;font-size:10px}
.about-photo{position:absolute;left:715px;top:105px;width:329px;height:396px;
  background:radial-gradient(ellipse at 50% 40%,#5a4034 0%,#22160f 40%,#050405 75%)}

/* contact band */
.touch{position:absolute;left:0;top:1370px;width:1200px;height:180px;background:var(--lilac-band);text-align:center}
.touch h2{position:absolute;left:0;width:1200px;top:25px;font-size:25px;font-weight:500}
.touch-btn{position:absolute;left:462px;top:92px;width:274px;height:31px;background:#fff;color:var(--purple);font-size:10.5px;font-weight:500;line-height:31px}

/* resume */
.h-sub{position:absolute;font-size:23px;font-weight:600;color:var(--ink)}
.rule-split{position:absolute;width:167px;height:3px;background:var(--purple-soft)}
.rule-split::before{content:"";position:absolute;left:0;top:0;width:55px;height:3px;background:var(--purple)}
.entry{position:absolute;left:177px;width:400px}
.entry .year{position:absolute;left:0;top:0;width:53px;height:20px;border:1px solid #999;font-size:10px;text-align:center;line-height:18px}
.entry .place{position:absolute;left:79px;top:3px;font-size:10px;color:var(--purple-bright)}
.entry h4{position:absolute;left:40px;top:33px;font-size:17px;font-weight:600;white-space:nowrap}
.entry p{position:absolute;left:40px;top:66px;width:360px;font-size:10px;line-height:19.5px;color:#444}
.tags{position:absolute;left:687px;width:380px;display:flex;flex-wrap:wrap;gap:11px 13px}
.tag{background:var(--purple);color:#fff;font-size:10px;height:21px;line-height:21px;padding:0 6px}
.cert{position:absolute;left:687px;width:357px;height:133px;border:2px solid var(--purple-soft)}
.cert .thumb{position:absolute;left:7px;top:7px;width:119px;height:115px;background:var(--lilac-card)}
.cert h4{position:absolute;left:143px;top:8px;font-size:17px;font-weight:600}
.cert p{position:absolute;left:143px;width:190px;font-size:10px;line-height:19.5px;color:#444}
.cert .date{color:var(--muted)}

/* blog */
.post{position:absolute;width:391px}
.post .pic{width:391px;height:217px}
.post .date{font-size:10px;color:var(--muted);margin-top:7px}
.post h4{font-size:17px;font-weight:600;margin-top:3px}
.post p{font-size:10px;line-height:19.5px;color:#444;margin-top:5px}
.load{position:absolute;left:177px;top:3707px;width:134px;height:31px;background:var(--purple);color:#fff;font-size:10.5px;text-align:center;line-height:31px}
</style>
</head>
<body>

<section class="hero">
  <nav class="sidebar">
    <svg style="top:340px" viewBox="0 0 14 14"><path d="M7 1 1 7h2v6h3V9h2v4h3V7h2z" fill="#fff"/></svg>
    <svg style="top:380px" viewBox="0 0 14 14" fill="none" stroke="#d9c5f5" stroke-width="1.4"><rect x="2" y="1.5" width="10" height="11" rx="1"/><circle cx="7" cy="6" r="1.8" fill="#d9c5f5"/><path d="M4.5 11c0-2 5-2 5 0"/></svg>
    <svg style="top:420px" viewBox="0 0 14 14" fill="none" stroke="#b79be0" stroke-width="1.3"><path d="M9 4v6a2 2 0 0 1-4 0V3a1.5 1.5 0 0 1 3 0v6.5a.5.5 0 0 1-1 0V4"/></svg>
  </nav>
  <div class="hero-photo" role="img" aria-label="Portrait photo of the site owner in profile against a dark background"></div>
  <h1 class="hero-name">Mira Solen</h1>
  <p class="hero-tag">Lorem ipsum dolor sit amet, consectetur adipiscing elit.<br>Faucibus integer tortor adipiscing dictum natoque.</p>
  <div class="social"><span>Journal</span><span>Circle</span><span>Work</span></div>
</section>

<section class="about">
  <h2 class="h-section" style="left:177px;top:105px">About Me</h2>
  <div class="rule" style="left:177px;top:148px"></div>
  <p style="top:183px">Lorem ipsum dolor sit amet, consectetur adipiscing elit. Ut sed orci vitae mattis tincidunt sagittis auctor feugiat et.</p>
  <p style="top:242px">Eu sodales nunc, risus nisl fusce at urna ultrices. Diam a diam in ultrices nulla. Habitasse habitant neque a, turpis diam lacus quisque. Tempor eu ornare interdum dui. Auctor diam nec, id vehicula metus sit lacus. Consectetur cursus viverra porta odio lacus felis quis.</p>
  <p style="top:339px">Aliquet eget sagittis, amet risus. Gravida viverra dictumst cras eget et enim sodales venenatis, faucibus.</p>
  <p class="fact" style="top:398px">Email:hello@mirasolen.com</p>
  <p class="fact" style="top:437px">Phone:+77 000 123 45 67</p>
  <p class="fact" style="top:476px">Study:University of Lakeside</p>
  <div class="about-photo" role="img" aria-label="Head-and-shoulders portrait of the site owner on a black background"></div>
</section>

<section class="touch">
  <h2>Let’s Get In Touch</h2>
  <div class="touch-btn">Let’s Get In Touch</div>
</section>

<section class="resume">
  <h2 class="h-section" style="left:177px;top:1652px">Resume</h2>
  <div class="rule" style="left:177px;top:1699px"></div>

  <h3 class="h-sub" style="left:177px;top:1738px">Education</h3>
  <div class="rule-split" style="left:177px;top:1771px"></div>
  <div class="entry" style="top:1789px"><span class="year">2010</span><span class="place">University of Study</span><h4>Lorem Ipsum Dolor</h4><p>Lorem ipsum dolor sit amet, consectetur adipiscing elit. Ut sed orci vitae mattis tincidunt sagittis auctor feugiat et.</p></div>
  <div class="entry" style="top:1931px"><span class="year">2010</span><span class="place">University of Study</span><h4>Lorem Ipsum Dolor</h4><p>Lorem ipsum dolor sit amet, consectetur adipiscing elit. Ut sed orci vitae mattis tincidunt sagittis auctor feugiat et.</p></div>
  <div class="entry" style="top:2077px"><span class="year">2010</span><span class="place">University of Study</span><h4>Lorem Ipsum Dolor</h4><p>Lorem ipsum dolor sit amet, consectetur adipiscing elit. Ut sed orci vitae mattis tincidunt sagittis auctor feugiat et.</p></div>

  <h3 class="h-sub" style="left:177px;top:2263px">Experiences</h3>
  <div class="rule-split" style="left:177px;top:2296px"></div>
  <div class="entry" style="top:2314px"><span class="year">2010</span><span class="place">University of Study</span><h4>Lorem Ipsum Dolor</h4><p>Lorem ipsum dolor sit amet, consectetur adipiscing elit. Ut sed orci vitae mattis tincidunt sagittis auctor feugiat et.</p></div>
  <div class="entry" style="top:2455px"><span class="year">2010</span><span class="place">University of Study</span><h4>Lorem Ipsum Dolor</h4><p>Lorem ipsum dolor sit amet, consectetur adipiscing elit. Ut sed orci vitae mattis tincidunt sagittis auctor feugiat et.</p></div>
  <div class="entry" style="top:2602px"><span class="year">2010</span><span class="place">University of Study</span><h4>Lorem Ipsum Dolor</h4><p>Lorem ipsum dolor sit amet, consectetur adipiscing elit. Ut sed orci vitae mattis tincidunt sagittis auctor feugiat et.</p></div>

  <h3 class="h-sub" style="left:687px;top:1738px">Skills</h3>
  <div class="rule-split" style="left:687px;top:1771px"></div>
  <div class="tags" style="top:1794px"><span class="tag">Lorem Ipsum Dolor</span><span class="tag">Lorem Ipsum</span><span class="tag">Lorem Ipsum Dolor</span><span class="tag">Lorem Ipsum</span><span class="tag">Lorem Ipsum</span><span class="tag">Lorem Ipsum Dolor</span></div>

  <h3 class="h-sub" style="left:687px;top:1937px">Knowledges</h3>
  <div class="rule-split" style="left:687px;top:1970px"></div>
  <div class="tags" style="top:1992px"><span class="tag">Lorem Ipsum Dolor</span><span class="tag">Lorem Ipsum</span><span class="tag">Lorem Ipsum Dolor</span><span class="tag">Lorem Ipsum</span><span class="tag">Lorem Ipsum</span><span class="tag">Lorem Ipsum Dolor</span></div>

  <h3 class="h-sub" style="left:687px;top:2135px">Sertificates</h3>
  <div class="rule-split" style="left:687px;top:2168px"></div>
  <div class="cert" style="top:2190px"><div class="thumb"></div><h4>Lorem Ipsum Dolor</h4><p style="top:45px">Lorem ipsum dolor sit amet, consectetur adipiscing elit.</p><p class="date" style="top:92px">02 March 2009</p></div>
  <div class="cert" style="top:2350px"><div class="thumb"></div><h4>Lorem Ipsum Dolor</h4><p style="top:45px">Lorem ipsum dolor sit amet, consectetur adipiscing elit.</p><p class="date" style="top:92px">02 March 2009</p></div>
  <div class="cert" style="top:2510px"><div class="thumb"></div><h4>Lorem Ipsum Dolor</h4><p style="top:45px">Lorem ipsum dolor sit amet, consectetur adipiscing elit.</p><p class="date" style="top:92px">02 March 2009</p></div>
</section>

<section class="blog">
  <h2 class="h-section" style="left:177px;top:2857px">Blog</h2>
  <div class="rule" style="left:177px;top:2901px"></div>

  <article class="post" style="left:177px;top:2974px">
    <div class="pic" role="img" aria-label="Photo of two colleagues giving a high five at an office desk" style="background:linear-gradient(135deg,#8a6a58,#c9c2b8 50%,#6d6f74)"></div>
    <p class="date">02 March 2009</p><h4>Lorem Ipsum Dolor</h4>
    <p>Lorem ipsum dolor sit amet, consectetur adipiscing elit. Ut sed orci vitae mattis tincidunt sagittis auctor feugiat et.</p>
  </article>
  <article class="post" style="left:654px;top:2974px">
    <div class="pic" role="img" aria-label="Photo of a person in a suit reading a newspaper" style="background:linear-gradient(135deg,#bfc1c4,#e4e4e4 45%,#3a3b40)"></div>
    <p class="date">02 March 2009</p><h4>Lorem Ipsum Dolor</h4>
    <p>Lorem ipsum dolor sit amet, consectetur adipiscing elit. Ut sed orci vitae mattis tincidunt sagittis auctor feugiat et.</p>
  </article>
  <article class="post" style="left:177px;top:3360px">
    <div class="pic" role="img" aria-label="Photo of hands holding a phone over printed charts on a wooden desk" style="background:linear-gradient(135deg,#c08a5a,#e9dccd 55%,#b7794a)"></div>
    <p class="date">02 March 2009</p><h4>Lorem Ipsum Dolor</h4>
    <p>Lorem ipsum dolor sit amet, consectetur adipiscing elit. Ut sed orci vitae mattis tincidunt sagittis auctor feugiat et.</p>
  </article>
  <article class="post" style="left:654px;top:3360px">
    <div class="pic" role="img" aria-label="Photo of a stock line chart on a screen" style="background:linear-gradient(135deg,#f2f2f2,#dcdcdc 60%,#2a2a2a)"></div>
    <p class="date">02 March 2009</p><h4>Lorem Ipsum Dolor</h4>
    <p>Lorem ipsum dolor sit amet, consectetur adipiscing elit. Ut sed orci vitae mattis tincidunt sagittis auctor feugiat et.</p>
  </article>

  <div class="load">Load More</div>
</section>

</body>
</html>
```